designing a website for a vacation beach house rental

We are buying a vacation rental on an awesome beach on the Isle of Palms in South Carolina. The closing is not until November 30 so we will only have the photos from the current home and we can change the photos once we move our furniture in. We want the website to be exciting and interactive and for people to be able to go to a chatterly page (that needs to be created) and the name of the beach house needs to be created (the address is 462 Marlowe Crescent, Isle of Palms. We need to be able to take this site and add it to KLNZ and StayNest and Dune Q&Q and other travel sites. We need the person that clicks on it to be hooked from the first second. We think this one is pretty good but we want ours way better http://gullrestcottage.example/ The price per week will be $7200 so the website needs to be elegant, stunning, all inclusive, retreat, relaxing, friends and family, eating together, amazing food town, beaches, golf, cocktails, wine, restaurants, history, architecture, opulence, Look up Charleston, SC to get an idea of what the area is all about. Top Chefs and top wines.

Target Market(s)

Upper class families with children; classy dressing; golfers; foodies; wine lovers; in shaper beach goers living the dream of a gorgeous beach house with friends and family at the pool, eating together, beach together, cooking together, playing games, walking on the beach, running on the beach, watching the sunset on the beach

Industry/Entity Type

House

Logo Text

the look and feel of an upper class family on vacation in an exclusive resort

Number of Pages Required

5+ page

Font styles to use
Serif

Requirements
Must have
• Lots of photos and movement; easy for me to update is a MUST; easy for a guest to register for staying; a calendar that will update automatically when someone pays; ability to take credit cards and CoinTap; guest book; keep up with the number of visits; all of the bells and whistles of the most modern websites; also works on any device like Zelphone or Zelpad or any smartphone

```html
<!DOCTYPE html>
<html lang="en">
<head>
<meta charset="utf-8">
<title>Seabright Haven Beach House</title>
<link rel="stylesheet" href="https://fonts.googleapis.com/css2?family=Inter:wght@300;400;500;600&family=Open+Sans:ital,wght@0,400;1,400&display=swap">
<style>
:root{
  --accent:#f7a400;
  --accent-deep:#e98d00;
  --ink:#111111;
  --body:#333333;
  --muted:#9a9a9a;
  --white:#ffffff;
  --nav:#1b1b1b;
  --dot:#d2d2d2;
}
*{margin:0;padding:0;box-sizing:border-box}
html,body{width:1200px;height:2719px;overflow:hidden;background:var(--white)}
body{position:relative;font-family:"Inter",Arial,sans-serif;color:var(--body)}
.abs{position:absolute}

/* Navigation */
.site-nav{left:0;top:0;width:1200px;height:49px;background:var(--nav)}
.brand{left:36px;top:14px;display:flex;align-items:center;gap:8px;color:var(--accent);font-size:14px;font-weight:500;white-space:nowrap}
.brand-dot{width:20px;height:20px;border-radius:50%;background:var(--accent)}
.nav-link{top:17px;font-size:13px;color:var(--white);white-space:nowrap}
.nav-link.is-active{color:var(--accent)}
.nav-link.is-active::after{content:"";position:absolute;left:-8px;right:-8px;top:29px;height:2px;background:var(--accent)}
.nav-book{left:1095px;top:11px;width:88px;height:28px;border-radius:14px;background:var(--accent);color:var(--white);font-size:13px;display:flex;align-items:center;justify-content:center}

/* Hero */
.hero{left:0;top:49px;width:1200px;height:625px;overflow:hidden;background:
  radial-gradient(circle at 300px 340px,#ffe9a8 0,#f9b640 12%,rgba(230,120,20,.6) 30%,transparent 55%),
  linear-gradient(180deg,#3a3a48 0%,#7d5a4a 30%,#e08a2a 58%,#7a3e12 72%,#2a1608 100%)}
.hero-title{left:0;width:1200px;top:212px;text-align:center;color:var(--white);font-size:72px;line-height:88px;font-weight:300;letter-spacing:1px;white-space:nowrap}
.hero-sub{left:790px;top:300px;color:var(--white);font-size:24px;line-height:30px;font-weight:300;letter-spacing:2px;white-space:nowrap}
.hero-arrow{top:272px;width:32px;height:32px;border-radius:50%;display:flex;align-items:center;justify-content:center}
.hero-arrow.prev{left:37px;background:var(--accent-deep)}
.hero-arrow.next{left:1130px;background:#1a1a1a}
.scroll-cue{left:591px;top:553px;width:18px;height:30px;border:2px solid var(--white);border-radius:9px}
.scroll-cue::after{content:"";position:absolute;left:6px;top:6px;width:2px;height:6px;background:var(--white);border-radius:1px}

/* Feature cards */
.features{left:0;top:674px;width:1200px;height:305px;background:var(--white)}
.feature{top:18px;width:210px;height:265px;text-align:center;border:3px solid transparent;border-radius:8px}
.feature.is-selected{border-color:var(--accent);box-shadow:0 2px 8px rgba(0,0,0,.08)}
.feature svg{margin-top:30px}
.feature h3{font-size:12px;font-weight:600;color:var(--ink);margin-top:22px;letter-spacing:.2px}
.feature p{font-size:10.5px;line-height:14px;color:var(--muted);margin-top:12px}
.pill{display:inline-flex;align-items:center;justify-content:center;border:1.5px solid var(--accent);color:var(--accent);border-radius:16px;font-size:12px;white-space:nowrap}
.feature .pill{width:100px;height:30px;margin-top:18px}
.feature.is-selected .pill{background:var(--accent);color:var(--white)}

/* Story sections */
.story{left:0;width:1200px}
.story-explore{top:979px;height:482px;background:linear-gradient(180deg,#5a4a3a 0%,#a87042 45%,#e3a04a 70%,#7a4d2a 100%)}
.story-relax{top:1670px;height:487px;background:linear-gradient(180deg,#9fb6c0 0%,#c9d5d4 40%,#7fa3a8 70%,#5d8b93 100%)}
.story-card{background:var(--white);border-radius:4px;box-shadow:0 6px 24px rgba(0,0,0,.18)}
.photo-frame{background:var(--white);padding:8px;box-shadow:0 8px 24px rgba(0,0,0,.3)}
.photo{width:100%;height:100%}
.photo-swing{background:linear-gradient(160deg,#3b2a20 0%,#b8681c 45%,#ffd37a 70%,#6a3510 100%)}
.photo-lake{background:linear-gradient(180deg,#d6e2e4 0%,#b7ccd0 40%,#6f9aa2 65%,#c8b8a4 100%)}
.story h2{font-size:31px;line-height:38px;font-weight:300;color:var(--ink);white-space:nowrap}
.story-copy{font-family:"Open Sans",Arial,sans-serif;font-style:italic;font-size:16.5px;line-height:22px;color:var(--muted);text-align:justify}
.story .pill{width:110px;height:31px}

/* Testimonials */
.testimonial{left:0;width:1200px;background:var(--white);text-align:center}
.quote{color:var(--ink);margin:0 auto}
.quote-lg{font-size:21px;line-height:25px;font-weight:300}
.quote-sm{font-size:14.5px;line-height:19px;font-weight:300;width:726px;color:#333;text-align:justify;text-align-last:center}
.cite{font-size:14px;color:var(--ink);font-weight:400}
.dots{display:flex;justify-content:center;gap:6px}
.dots span{width:6px;height:6px;border-radius:50%;background:var(--dot)}
.dots span.on{width:8px;height:8px;background:var(--accent);margin-top:-1px}

/* Closing banner */
.closing{left:0;top:2416px;width:1200px;height:285px;background:
  linear-gradient(180deg,#5a3a30 0%,#c86a2a 40%,#e58a30 55%,#7a3a16 80%,#3a1a0a 100%)}
.closing-quote{left:0;width:1200px;top:90px;text-align:center;color:var(--white);font-size:41px;line-height:50px;font-weight:300}
.closing-cite{left:0;width:1200px;top:143px;text-align:center;color:var(--white);font-size:14px}
.to-top{left:1166px;top:245px;width:18px;height:20px;background:#222;border-radius:2px;display:flex;align-items:center;justify-content:center}

/* Footer */
.site-footer{left:0;top:2701px;width:1200px;height:18px;background:#1a1a1a}
.legal{left:0;width:1200px;top:3px;text-align:center;color:#777;font-size:9px}
.social{top:4px;width:11px;height:11px;border-radius:50%;background:#666}
</style>
</head>
<body>

<header class="abs site-nav">
  <div class="abs brand"><span class="brand-dot"></span>Seabright Haven</div>
  <span class="abs nav-link is-active" style="left:700px">Home</span>
  <span class="abs nav-link" style="left:803px">About</span>
  <span class="abs nav-link" style="left:890px">Things to Do</span>
  <span class="abs nav-link" style="left:1003px">Contact Us</span>
  <span class="abs nav-book">Book Now</span>
</header>

<section class="abs hero" role="img" aria-label="Photo of a surfer carrying a board along the shore at sunset">
  <div class="abs hero-title">Seabright Haven</div>
  <div class="abs hero-sub">BEACH HOUSE</div>
  <div class="abs hero-arrow prev"><svg width="10" height="12" viewBox="0 0 10 12"><path d="M7 1 2 6l5 5" fill="none" stroke="#fff" stroke-width="2"/></svg></div>
  <div class="abs hero-arrow next"><svg width="10" height="12" viewBox="0 0 10 12"><path d="M3 1l5 5-5 5" fill="none" stroke="#f7a400" stroke-width="2"/></svg></div>
  <div class="abs scroll-cue"></div>
</section>

<section class="abs features">
  <div class="abs feature is-selected" style="left:143px">
    <svg width="70" height="50" viewBox="0 0 70 50" fill="none" stroke="#f7a400" stroke-width="2">
      <path d="M8 24 30 8l22 16"/><path d="M13 21v22h34V21"/><rect x="25" y="30" width="10" height="13"/><rect x="16" y="26" width="6" height="6"/><rect x="38" y="26" width="6" height="6"/><path d="M4 44h62"/><path d="M58 44V30"/><circle cx="58" cy="24" r="7"/>
    </svg>
    <h3>ABOUT THE HOME</h3>
    <p>We love our beach house!<br>Let me tell you a few things about it!</p>
    <span class="pill">Know more</span>
  </div>
  <div class="abs feature" style="left:379px">
    <svg width="70" height="50" viewBox="0 0 70 50" fill="none" stroke="#f7a400" stroke-width="2">
      <ellipse cx="35" cy="25" rx="6" ry="22"/><path d="M35 8v34"/><path d="M18 25h34"/>
    </svg>
    <h3>THINGS TO DO</h3>
    <p>We love our beach house!<br>Let me tell you a few things about it!</p>
    <span class="pill">Know more</span>
  </div>
  <div class="abs feature" style="left:622px">
    <svg width="70" height="50" viewBox="0 0 70 50" fill="none" stroke="#f7a400" stroke-width="2">
      <path d="M35 46s-14-15-14-25a14 14 0 0 1 28 0c0 10-14 25-14 25z"/><circle cx="35" cy="21" r="5"/>
    </svg>
    <h3>GETTING HERE</h3>
    <p>We love our beach house!<br>Let me tell you a few things about it!</p>
    <span class="pill">Know more</span>
  </div>
  <div class="abs feature" style="left:847px">
    <svg width="70" height="50" viewBox="0 0 70 50" fill="none" stroke="#f7a400" stroke-width="2">
      <rect x="20" y="10" width="30" height="34" rx="3"/><path d="M20 19h30M27 5v9M43 5v9"/><path d="M28 31l5 5 9-9"/>
    </svg>
    <h3>BOOK NOW</h3>
    <p>We love our beach house!<br>Let me tell you a few things about it!</p>
    <span class="pill">Book Now</span>
  </div>
</section>

<section class="abs story story-explore" aria-label="Explore section">
  <div class="abs story-card" style="left:109px;top:87px;width:990px;height:305px"></div>
  <div class="abs photo-frame" style="left:134px;top:51px;width:522px;height:373px">
    <div class="photo photo-swing" role="img" aria-label="Photo of a woman on a swing against the setting sun"></div>
  </div>
  <h2 class="abs" style="left:707px;top:125px">Explore Your Dream</h2>
  <p class="abs story-copy" style="left:707px;top:177px;width:319px">Contrary to popular belief, Lorem Ipsum is not simply random text. It has roots in a piece of classical Latin literature from 45 BC, making it over 2000 years old.</p>
  <span class="abs pill" style="left:707px;top:278px">Explore Now</span>
</section>

<section class="abs testimonial" style="top:1461px;height:209px">
  <p class="quote quote-lg" style="margin-top:65px">“Very clean with a lot of amenities! Very comfy for entertaining as well.<br>The owner and Reuben were wonderful.”</p>
  <p class="cite" style="margin-top:18px">Guest, Australia</p>
  <div class="dots" style="margin-top:38px"><span class="on"></span><span></span><span></span><span></span><span></span></div>
</section>

<section class="abs story story-relax" aria-label="Relax section">
  <div class="abs story-card" style="left:109px;top:92px;width:990px;height:303px"></div>
  <h2 class="abs" style="left:156px;top:134px">Come and Relax</h2>
  <p class="abs story-copy" style="left:156px;top:185px;width:319px">Contrary to popular belief, Lorem Ipsum is not simply random text. It has roots in a piece of classical Latin literature from 45 BC, making it over 2000 years old.</p>
  <span class="abs pill" style="left:156px;top:286px">Explore Now</span>
  <div class="abs photo-frame" style="left:549px;top:57px;width:522px;height:370px">
    <div class="photo photo-lake" role="img" aria-label="Photo of a woman in white resting by the water"></div>
  </div>
</section>

<section class="abs testimonial" style="top:2157px;height:259px">
  <p class="quote quote-sm" style="margin-top:67px">“When we entered the condo we noticed how clean everything was and we immediately felt at ease. It was great to have a washer and dryer. The beds were all comfortable and the rooms were spacious. After sightseeing all day it was nice to relax and watch TV. The kitchen was well stocked for our needs. We all enjoyed sitting on the back deck and relaxing.”</p>
  <p class="cite" style="margin-top:24px">Guest, New York</p>
  <div class="dots" style="margin-top:52px"><span class="on"></span><span></span><span></span><span></span><span></span></div>
</section>

<section class="abs closing" role="img" aria-label="Photo of a family walking along the beach at sunset with hills behind">
  <div class="abs closing-quote">“Happiest moment in my life ever”</div>
  <div class="abs closing-cite">Lena Harwick, United States</div>
  <div class="abs to-top"><svg width="8" height="10" viewBox="0 0 8 10"><path d="M1 5l3-3 3 3M1 9l3-3 3 3" fill="none" stroke="#fff" stroke-width="1.2"/></svg></div>
</section>

<footer class="abs site-footer">
  <div class="abs legal">All Rights Reserved.</div>
  <span class="abs social" style="left:1148px"></span>
  <span class="abs social" style="left:1168px"></span>
</footer>

</body>
</html>
```